Gestalten Sie ein tolles Selbstliebe-Buchcover
Design kam bei der Zielgruppe sehr gut an und war professionell umgesetzt. Die Kommunikation läuft zielgerichtet und nett und ich habe schnell alle Dateien bekommen, die ich brauche. Vielen Dank!
Hallo,
schön, dass Sie sich für diese Ausschreibung interessieren. Wir suchen ein Cover für unser Buch, das wir im Selbstverlag veröffentlichen werden.
Titel: Mondgarten am Nordufer
Untertitel 1: Wie du dich von negativen Gedanken befreist und eine liebevolle Beziehung zu dir selbst aufbaust
Untertitel Teil 2: 12 lebensverändernde Monate voller positiver Impulse und Liebe für dich
Das Buch soll (mehrheitlich) Frauen unterstützen, eine liebevolle Beziehung zu sich selbst aufzubauen, negative Gedanken loszulassen und innere Ruhe zu finden.
Aufgabenstellung
Wir sind für jegliche Vorschläge im Rahmen des Themas, der Samples und der Schieberegler offen.
Wichtig ist allerdings
- dass das Design selbst in der kleinen Ansicht (Suchergebnisse) auf Vendora klar hervorsticht, das heißt dort klar erkennbar und die Schrift sofort lesbar ist. Es muss in klein „wirken“, weil viele mit dem Handy auf Vendora shoppen und die Ansicht in den Suchergebnissen dort noch kleiner ist.
- dass das Design die gezielt Emotionen vermittelt
Optimal wäre es, wenn Ihr keine Mockups hochladet. Das macht es viel schwieriger, die Designs einzuschätzen und miteinander zu vergleichen.

```html
<!DOCTYPE html>
<html lang="de">
<head>
<meta charset="utf-8">
<title>Mondgarten am Nordufer – Buchcover</title>
<link rel="stylesheet" href="https://fonts.googleapis.com/css2?family=Dancing+Script:wght@700&family=Great+Vibes&family=Archivo:ital,wght@0,500;0,700;1,800&display=swap">
<style>
  :root {
    --paper-light: #fbe3e4;
    --paper-mid: #f6c9cb;
    --paper-deep: #eea5a9;
    --ink: #111111;
    --title-pink: #e9506b;
    --accent-red: #c3202f;
    --panel: rgba(255, 248, 246, 0.62);
    --rose-tone: #e8808f;
    --heart-tone: #d4243a;
    --heart-deep: #b8162c;
    --wing-tone: #fdf3f3;
  }
  * { margin: 0; padding: 0; box-sizing: border-box; }
  html, body { width: 800px; height: 1200px; overflow: hidden; }
  body { background: var(--paper-light); }
  .cover {
    position: relative;
    width: 800px;
    height: 1200px;
    overflow: hidden;
    background:
      radial-gradient(ellipse 420px 300px at 15% 10%, rgba(238,165,169,0.55), transparent 70%),
      radial-gradient(ellipse 380px 300px at 90% 30%, rgba(238,165,169,0.45), transparent 70%),
      radial-gradient(ellipse 460px 320px at 20% 75%, rgba(238,165,169,0.5), transparent 70%),
      radial-gradient(ellipse 400px 300px at 85% 95%, rgba(238,165,169,0.45), transparent 70%),
      linear-gradient(160deg, var(--paper-mid), var(--paper-light) 45%, var(--paper-mid));
  }
  .title-main {
    position: absolute;
    top: 70px;
    left: 0;
    width: 800px;
    text-align: center;
    font-family: "Dancing Script", cursive;
    font-weight: 700;
    font-size: 168px;
    line-height: 1;
    color: var(--ink);
  }
  .title-sub {
    position: absolute;
    top: 268px;
    left: 0;
    width: 800px;
    text-align: center;
    font-family: "Great Vibes", cursive;
    font-weight: 400;
    font-size: 118px;
    line-height: 1;
    color: var(--title-pink);
  }
  .subtitle-panel {
    position: absolute;
    left: 250px;
    top: 485px;
    width: 550px;
    height: 198px;
    background: var(--panel);
  }
  .subtitle-text {
    position: absolute;
    left: 349px;
    top: 505px;
    width: 451px;
    font-family: "Archivo", sans-serif;
    font-weight: 500;
    font-size: 26px;
    line-height: 35px;
    text-transform: uppercase;
    white-space: nowrap;
    color: var(--ink);
  }
  .rose-art {
    position: absolute;
    left: 157px;
    top: 437px;
    width: 164px;
    height: 304px;
  }
  .tagline {
    position: absolute;
    top: 758px;
    left: 0;
    width: 800px;
    padding-right: 18px;
    text-align: center;
    font-family: "Archivo", sans-serif;
    font-style: italic;
    font-weight: 800;
    font-size: 25px;
    line-height: 32px;
    text-transform: uppercase;
    color: var(--accent-red);
  }
  .wings-heart-art {
    position: absolute;
    left: 35px;
    top: 790px;
    width: 733px;
    height: 330px;
  }
  .author {
    position: absolute;
    top: 1135px;
    left: 0;
    width: 800px;
    text-align: center;
    font-family: "Archivo", sans-serif;
    font-weight: 700;
    font-size: 26px;
    letter-spacing: 0.56em;
    text-indent: 0.56em;
    text-transform: uppercase;
    color: var(--ink);
  }
</style>
</head>
<body>
<main class="cover">
  <h1>
    <span class="title-main">Mondgarten</span>
    <span class="title-sub">am Nordufer</span>
  </h1>

  <div class="subtitle-panel"></div>
  <svg class="rose-art" viewBox="0 0 164 304" role="img" aria-label="Illustration: Rosenzweig mit einer roten Blüte und gezeichneten Blättern">
    <defs>
      <linearGradient id="roseFill" x1="0" y1="0" x2="0" y2="1">
        <stop offset="0" stop-color="#f3c2c7" stop-opacity="0.6"/>
        <stop offset="0.45" stop-color="var(--rose-tone)" stop-opacity="0.8"/>
        <stop offset="1" stop-color="#f3c2c7" stop-opacity="0.5"/>
      </linearGradient>
    </defs>
    <rect width="164" height="304" rx="14" fill="url(#roseFill)"/>
  </svg>
  <p class="subtitle-text">Wie du dich von negativen<br>Gedanken befreist und<br>eine liebevolle Beziehung<br>zu dir selbst aufbaust</p>

  <svg class="wings-heart-art" viewBox="0 0 733 330" role="img" aria-label="Illustration: rotes Aquarell-Herz mit ausgebreiteten Engelsflügeln">
    <defs>
      <radialGradient id="wingFill" cx="0.5" cy="0.5" r="0.5">
        <stop offset="0" stop-color="var(--wing-tone)" stop-opacity="0.9"/>
        <stop offset="0.7" stop-color="var(--wing-tone)" stop-opacity="0.55"/>
        <stop offset="1" stop-color="var(--wing-tone)" stop-opacity="0"/>
      </radialGradient>
      <linearGradient id="heartFill" x1="0" y1="0" x2="1" y2="1">
        <stop offset="0" stop-color="var(--heart-tone)"/>
        <stop offset="0.55" stop-color="#dc3a50"/>
        <stop offset="1" stop-color="var(--heart-deep)"/>
      </linearGradient>
    </defs>
    <ellipse cx="200" cy="125" rx="200" ry="80" transform="rotate(22 200 125)" fill="url(#wingFill)"/>
    <ellipse cx="533" cy="125" rx="200" ry="80" transform="rotate(-22 533 125)" fill="url(#wingFill)"/>
    <path d="M365 138 C340 86 228 80 226 168 C224 244 318 284 365 326 C412 284 506 244 504 168 C502 80 390 86 365 138 Z"
          fill="url(#heartFill)" stroke="#ffffff" stroke-width="5"/>
    <path d="M365 138 C340 86 228 80 226 168 C224 244 318 284 365 326 C412 284 506 244 504 168 C502 80 390 86 365 138 Z"
          fill="none" stroke="#8a7a7a" stroke-width="1" transform="translate(0 0)"/>
  </svg>
  <p class="tagline">12 lebensverändernde Monate<br>voller positiver Impulse und Liebe<br>für dich</p>

  <p class="author">Luis Voringer</p>
</main>
</body>
</html>
```